Steady Rig Vitals: Truck Smoke Check Company

I need a logo for a truck health company in California called "Steady Rig Vitals". This company does smoke checks for heavy duty diesel trucks under the Western Clean Skies Council (WCSC) called HD I/M tests. I want the brand to feel reliable.

Target Market(s)

California Diesel Trucks. Individual truck drivers and trucking companies.

Industry/Entity Type

Automotive

Contact Information for Business Card

Company Name, Slogan, contact information. marcusbell@steadyrigvitals.example

```html
<!DOCTYPE html>
<html lang="en">
<head>
<meta charset="utf-8">
<title>Steady Rig Vitals – Business Card</title>
<link href="https://fonts.googleapis.com/css2?family=Montserrat:wght@400;500;600;700&display=swap" rel="stylesheet">
<style>
  :root {
    --backdrop: #d6d6d6;
    --card-black: #000000;
    --card-white: #ffffff;
    --ink-light: #ffffff;
    --ink-dark: #111111;
    --slogan-grey: #6a6a6a;
    --rule-grey: #555555;
    --smoke-core: rgba(200,200,200,0.38);
    --smoke-edge: rgba(120,120,120,0);
  }
  * { box-sizing: border-box; margin: 0; padding: 0; }
  html, body {
    width: 1200px; height: 1200px; overflow: hidden;
    background: var(--backdrop);
    font-family: "Montserrat", sans-serif;
  }
  .card {
    position: absolute; left: 120px; width: 960px; height: 548px;
    overflow: hidden; box-shadow: 0 6px 18px rgba(0,0,0,0.25);
  }
  .card--front { top: 40px; background: var(--card-black); }
  .card--back { top: 612px; background: var(--card-black); }

  .smoke {
    position: absolute;
    background: radial-gradient(ellipse at center, var(--smoke-core) 0%, rgba(150,150,150,0.15) 45%, var(--smoke-edge) 72%);
  }
  .card--front .smoke { left: 560px; top: 60px; width: 320px; height: 400px; }
  .card--back .smoke { right: -60px; top: 180px; width: 300px; height: 360px; }

  .brand-block {
    position: absolute; left: 0; right: 0; top: 222px; text-align: center;
  }
  .brand-name {
    color: var(--ink-light); font-weight: 600; font-size: 46px;
    letter-spacing: 2px; text-transform: uppercase;
  }
  .brand-slogan {
    color: var(--slogan-grey); font-weight: 400; font-size: 38px;
    margin-top: 4px; letter-spacing: 1px;
  }

  .identity-panel {
    position: absolute; left: 0; top: 0; width: 330px; height: 100%;
    background: var(--card-white);
  }
  .identity {
    position: absolute; left: 62px; top: 208px;
  }
  .identity-name {
    color: var(--ink-dark); font-weight: 700; font-size: 34px;
    letter-spacing: 2px; text-transform: uppercase;
  }
  .identity-role {
    color: var(--ink-dark); font-weight: 500; font-size: 20px;
    letter-spacing: 5px; text-transform: uppercase;
    display: inline-block; padding: 2px 10px 6px 18px;
    border-bottom: 2px solid var(--rule-grey);
  }

  .contact-panel {
    position: absolute; left: 330px; top: 0; right: 0; height: 100%;
  }
  .contact-brand {
    position: absolute; top: 60px; left: 0; right: 0; text-align: center;
    color: var(--ink-light); font-weight: 600; font-size: 26px;
    letter-spacing: 2px; text-transform: uppercase;
  }
  .contact-list {
    position: absolute; left: 70px; top: 140px; list-style: none;
  }
  .contact-item {
    display: flex; align-items: flex-start; gap: 20px;
    color: var(--ink-light); font-size: 26px; line-height: 1.45;
    margin-bottom: 22px; letter-spacing: 0.5px;
  }
  .contact-item--phone { font-size: 30px; font-weight: 500; letter-spacing: 2px; }
  .contact-icon {
    flex: none; width: 34px; height: 34px; margin-top: 3px;
    border-radius: 50%; background: var(--card-white);
    display: flex; align-items: center; justify-content: center;
  }
  .contact-icon svg { width: 20px; height: 20px; }
</style>
</head>
<body>

<section class="card card--front">
  <div class="smoke" role="img" aria-label="Soft grey drifting smoke wisps"></div>
  <div class="brand-block">
    <h1 class="brand-name">Steady Rig Vitals</h1>
    <p class="brand-slogan">Your Slogan Here</p>
  </div>
</section>

<section class="card card--back">
  <div class="smoke" role="img" aria-label="Soft grey drifting smoke wisps"></div>
  <div class="identity-panel">
    <div class="identity">
      <h2 class="identity-name">Marcus Bell</h2>
      <span class="identity-role">Director</span>
    </div>
  </div>
  <div class="contact-panel">
    <p class="contact-brand">Steady Rig Vitals</p>
    <ul class="contact-list">
      <li class="contact-item contact-item--phone">
        <span class="contact-icon"><svg viewBox="0 0 24 24"><path fill="#000" d="M6.6 10.8a15.1 15.1 0 0 0 6.6 6.6l2.2-2.2a1 1 0 0 1 1-.25 11.4 11.4 0 0 0 3.6.57 1 1 0 0 1 1 1V20a1 1 0 0 1-1 1A17 17 0 0 1 3 4a1 1 0 0 1 1-1h3.5a1 1 0 0 1 1 1c0 1.25.2 2.45.57 3.57a1 1 0 0 1-.25 1z"/></svg></span>
        <span>5550142786</span>
      </li>
      <li class="contact-item">
        <span class="contact-icon"><svg viewBox="0 0 24 24"><rect x="3" y="6" width="18" height="12" rx="1.5" fill="none" stroke="#000" stroke-width="2"/><path d="M3.5 7l8.5 6 8.5-6" fill="none" stroke="#000" stroke-width="2"/></svg></span>
        <span>marcusbell@steadyrigvitals.example</span>
      </li>
      <li class="contact-item">
        <span class="contact-icon"><svg viewBox="0 0 24 24"><circle cx="12" cy="12" r="9" fill="none" stroke="#000" stroke-width="2"/><ellipse cx="12" cy="12" rx="4" ry="9" fill="none" stroke="#000" stroke-width="1.6"/><path d="M3 12h18" stroke="#000" stroke-width="1.6"/></svg></span>
        <span>www.steadyrigvitals.example</span>
      </li>
      <li class="contact-item">
        <span class="contact-icon"><svg viewBox="0 0 24 24"><path fill="#000" d="M12 2a7 7 0 0 0-7 7c0 5.2 7 13 7 13s7-7.8 7-13a7 7 0 0 0-7-7zm0 9.5A2.5 2.5 0 1 1 12 6.5a2.5 2.5 0 0 1 0 5z"/></svg></span>
        <span>123 Anywhere St.,<br>Any City, ST 12345</span>
      </li>
    </ul>
  </div>
</section>

</body>
</html>
```